Bref créative
Veldmarkix
Security through insight
Simple
Tamsin Ruel
Co-Founder
Do not write an address
tamsin@veldmarkix.com
www.veldmarkix.com
Company logo located in the center of back business card.
Use only the "veldmarkix" logo without the cloud image from the .ai file.

```html
<!DOCTYPE html>
<html lang="en">
<head>
<meta charset="utf-8">
<title>Veldmarkix Stationery</title>
<link href="https://fonts.googleapis.com/css2?family=Open+Sans:wght@400;600;700&display=swap" rel="stylesheet">
<style>
  :root {
    --bg: #e4e5e7;
    --paper: #ffffff;
    --blue-deep: #163a6b;
    --blue: #1f5a99;
    --blue-light: #4d8fcf;
    --charcoal: #3a3b3d;
    --charcoal-dark: #222325;
    --ink: #4a4d52;
    --muted: #8a8d92;
    --line: #d3d5d8;
  }
  * { box-sizing: border-box; margin: 0; padding: 0; }
  html, body { width: 1200px; height: 439px; overflow: hidden; }
  body {
    background: linear-gradient(180deg, #eceded 0%, var(--bg) 100%);
    font-family: "Open Sans", Arial, sans-serif;
    color: var(--ink);
    position: relative;
  }
  .piece { position: absolute; background: var(--paper); overflow: hidden; }
  .piece svg.deco { position: absolute; inset: 0; width: 100%; height: 100%; }
  .caption { position: absolute; font-size: 6px; color: var(--muted); text-align: center; }

  .brand { display: flex; align-items: center; gap: 4px; position: absolute; white-space: nowrap; }
  .brand-dot { border-radius: 50%; background: var(--blue); flex: none; }
  .brand-name { font-weight: 700; color: var(--blue-deep); letter-spacing: 0.5px; }
  .brand-light .brand-name { color: #ffffff; }
  .brand-light .brand-dot { background: var(--blue-light); }

  /* business cards */
  .card { left: 22px; width: 104px; height: 94px; }
  .card-front { top: 65px; }
  .card-back { top: 182px; }
  .card-dark { top: 296px; background: linear-gradient(180deg, var(--charcoal) 0%, var(--charcoal-dark) 100%); }
  .card-front .brand { left: 6px; top: 44px; gap: 3px; }
  .card-front .brand-dot { width: 6px; height: 6px; }
  .card-front .brand-name { font-size: 6px; letter-spacing: 0.2px; }
  .card-person { position: absolute; left: 57px; top: 18px; font-size: 4px; line-height: 1.5; color: var(--ink); white-space: nowrap; }
  .card-person strong { display: block; font-size: 4.5px; color: var(--blue-deep); }
  .card-contact { position: absolute; left: 57px; top: 44px; font-size: 3.6px; line-height: 1.7; color: var(--ink); white-space: nowrap; }
  .card-back .brand, .card-dark .brand { left: 50%; top: 50%; transform: translate(-50%, -50%); }
  .card-back .brand-dot, .card-dark .brand-dot { width: 10px; height: 10px; }
  .card-back .brand-name, .card-dark .brand-name { font-size: 11px; }

  /* letterheads */
  .letterhead { top: 24px; width: 288px; height: 384px; }
  .letterhead-one { left: 204px; }
  .letterhead-two { left: 504px; }
  .letterhead .brand { left: 92px; top: 26px; }
  .letterhead .brand-dot { width: 12px; height: 12px; }
  .letterhead .brand-name { font-size: 12px; }
  .letterhead-contact { position: absolute; left: 196px; top: 26px; font-size: 4px; line-height: 1.8; color: var(--muted); border-left: 1px solid var(--line); padding-left: 5px; white-space: nowrap; }
  .letterhead-footer { position: absolute; left: 0; right: 0; bottom: 22px; text-align: center; font-size: 4px; color: var(--muted); }

  /* envelopes */
  .envelope { left: 811px; width: 377px; }
  .envelope-blue { top: 24px; height: 100px; }
  .envelope-dark { top: 108px; height: 100px; }
  .envelope-plain { top: 182px; height: 105px; }
  .envelope-front { top: 259px; height: 148px; }
  .envelope-blue .brand, .envelope-dark .brand { left: 50%; top: 40px; transform: translateX(-50%); }
  .envelope .brand-dot { width: 9px; height: 9px; }
  .envelope .brand-name { font-size: 9px; }
  .envelope-front .brand { left: 18px; top: 24px; }
  .envelope-front .brand-dot { width: 12px; height: 12px; }
  .envelope-front .brand-name { font-size: 12px; }
</style>
</head>
<body>

  <!-- business card front -->
  <div class="piece card card-front">
    <svg class="deco" viewBox="0 0 104 94" preserveAspectRatio="none" aria-hidden="true">
      <path d="M0 0 H26 Q8 10 0 30 Z" fill="var(--blue-deep)"/>
      <path d="M104 94 H74 Q96 84 104 62 Z" fill="var(--blue)"/>
    </svg>
    <div class="brand"><span class="brand-dot"></span><span class="brand-name">Veldmarkix</span></div>
    <div class="card-person"><strong>Tamsin Ruel</strong>Co-Founder</div>
    <div class="card-contact">tamsin@veldmarkix.com<br>www.veldmarkix.com</div>
  </div>
  <div class="caption" style="left:22px;top:162px;width:104px;">Front business card</div>

  <!-- business card back -->
  <div class="piece card card-back">
    <svg class="deco" viewBox="0 0 104 94" preserveAspectRatio="none" aria-hidden="true">
      <path d="M104 94 H70 Q96 82 104 56 Z" fill="var(--blue)"/>
    </svg>
    <div class="brand"><span class="brand-dot"></span><span class="brand-name">Veldmarkix</span></div>
  </div>
  <div class="caption" style="left:22px;top:279px;width:104px;">Back business card</div>

  <!-- business card dark -->
  <div class="piece card card-dark">
    <div class="brand brand-light"><span class="brand-dot"></span><span class="brand-name">Veldmarkix</span></div>
  </div>
  <div class="caption" style="left:22px;top:393px;width:104px;">Back dark card</div>

  <!-- letterhead one -->
  <div class="piece letterhead letterhead-one">
    <svg class="deco" viewBox="0 0 288 384" preserveAspectRatio="none" aria-hidden="true">
      <path d="M0 0 H62 Q18 18 0 70 Z" fill="var(--blue-deep)"/>
      <path d="M0 0 H74 Q26 22 0 82" fill="none" stroke="var(--blue-light)" stroke-width="1.5"/>
      <path d="M288 384 H230 Q274 366 288 320 Z" fill="var(--blue-deep)"/>
      <path d="M288 384 H218 Q266 362 288 308" fill="none" stroke="var(--blue-light)" stroke-width="1.5"/>
    </svg>
    <div class="brand"><span class="brand-dot"></span><span class="brand-name">Veldmarkix</span></div>
    <div class="letterhead-contact">tamsin@veldmarkix.com<br>www.veldmarkix.com</div>
  </div>
  <div class="caption" style="left:204px;top:412px;width:288px;">Letterhead first page</div>

  <!-- letterhead two -->
  <div class="piece letterhead letterhead-two">
    <svg class="deco" viewBox="0 0 288 384" preserveAspectRatio="none" aria-hidden="true">
      <path d="M0 0 H62 Q18 18 0 70 Z" fill="var(--blue-deep)"/>
      <path d="M0 0 H74 Q26 22 0 82" fill="none" stroke="var(--blue-light)" stroke-width="1.5"/>
      <path d="M288 384 H230 Q274 366 288 320 Z" fill="var(--blue-deep)"/>
      <path d="M288 384 H218 Q266 362 288 308" fill="none" stroke="var(--blue-light)" stroke-width="1.5"/>
    </svg>
    <div class="letterhead-footer">tamsin@veldmarkix.com &nbsp;|&nbsp; www.veldmarkix.com</div>
  </div>
  <div class="caption" style="left:504px;top:412px;width:288px;">Letterhead second page</div>

  <!-- envelope with blue flap -->
  <div class="piece envelope envelope-blue">
    <svg class="deco" viewBox="0 0 377 100" preserveAspectRatio="none" aria-hidden="true">
      <defs>
        <linearGradient id="flapBlue" x1="0" y1="0" x2="0" y2="1">
          <stop offset="0" stop-color="#2d6fb3"/><stop offset="1" stop-color="var(--blue-deep)"/>
        </linearGradient>
      </defs>
      <path d="M0 0 H377 V18 Q188 40 0 18 Z" fill="url(#flapBlue)"/>
    </svg>
    <div class="brand"><span class="brand-dot"></span><span class="brand-name">Veldmarkix</span></div>
  </div>

  <!-- envelope with dark flap -->
  <div class="piece envelope envelope-dark">
    <svg class="deco" viewBox="0 0 377 100" preserveAspectRatio="none" aria-hidden="true">
      <defs>
        <linearGradient id="flapDark" x1="0" y1="0" x2="0" y2="1">
          <stop offset="0" stop-color="#55575a"/><stop offset="1" stop-color="var(--charcoal-dark)"/>
        </linearGradient>
      </defs>
      <path d="M0 0 H377 V18 Q188 40 0 18 Z" fill="url(#flapDark)"/>
    </svg>
    <div class="brand"><span class="brand-dot"></span><span class="brand-name">Veldmarkix</span></div>
  </div>

  <!-- plain envelope back -->
  <div class="piece envelope envelope-plain">
    <svg class="deco" viewBox="0 0 377 105" preserveAspectRatio="none" aria-hidden="true">
      <path d="M0 0 L188 60 L377 0" fill="none" stroke="var(--line)" stroke-width="1"/>
      <path d="M0 105 L150 48 M377 105 L226 48" fill="none" stroke="var(--line)" stroke-width="1"/>
    </svg>
  </div>

  <!-- envelope front -->
  <div class="piece envelope envelope-front">
    <svg class="deco" viewBox="0 0 377 148" preserveAspectRatio="none" aria-hidden="true">
      <path d="M377 148 H300 Q360 132 377 90 Z" fill="var(--blue-deep)"/>
      <path d="M377 148 H286 Q350 128 377 78" fill="none" stroke="var(--blue-light)" stroke-width="1.5"/>
    </svg>
    <div class="brand"><span class="brand-dot"></span><span class="brand-name">Veldmarkix</span></div>
  </div>
  <div class="caption" style="left:811px;top:412px;width:377px;">Envelope set</div>

</body>
</html>
```